Business card design needed for rebranded top-end landscaping business

We need a new business card design, incorporating our logo (colours Green #8dc63f and Grey #8a8c8e) and also some options that include the colour dark navy (eg #000040) as our uniforms are navy with white and grey trim.

We are an innovative landscaping company that maintains high-end gardens for meticulous clients. We pride ourselves on our customer service, our professionalism, and our workmanship.

Our business name needs to be easily read and our branding needs to be bold and memorable, without screaming "tradesman"! We prefer clean lines over lots of fine detail.

The design MUST include:
- Business name ("Brambleton Gardenworks")
- Logo (file uploaded)
- Employee name
- Phone number
- Email address
- www.brambletongardenworks.com.au
- Facebook & Instagram logos
- The Turfcraft Guild logo (file uploaded) along with the word "Member"
- Licence "Lic. 618392K"

OPTIONAL inclusions:
- "Creating outdoor spaces for our community to be inspired, refreshed and re-energised"
- "Landscape Maintenance - Irrigation - Arboriculture" (dashes can be replaced with dots or other)
- "Fully qualified, licensed & insured"
- "Residential - Strata - Commercial - Real Estate" (dashes can be replaced with dots or other)

High-end professionals and retirees, real estate agents

Landscaping

See Project description

Sans Serif

Designer to choose colors to be used in the design.

• Must incorporate our logo, and colours Green #8dc63f and Grey #8a8c8e) from the logo, and the colour DARK NAVY (eg #000040).
• The design MUST include:
• - Business name ("Brambleton Gardenworks")
• - Logo (file uploaded)
• - Employee name
• - Phone number
• - Email address
• - www.brambletongardenworks.com.au
• - Facebook & Instagram logos
• - The Turfcraft Guild logo (file uploaded) along with the word "Member"
• - Licence "Lic. 618392K"
• OPTIONAL inclusions:
• - "Creating outdoor spaces for our community to be inspired, refreshed and re-energised"
• - "Landscape Maintenance - Irrigation - Arboriculture" (dashes can be replaced with dots or other)
• - "Fully qualified, licensed & insured"
• - "Residential - Strata - Commercial - Real Estate" (dashes can be replaced with dots or other)

```html
<!DOCTYPE html>
<html lang="en">
<head>
<meta charset="utf-8">
<title>Brambleton Gardenworks – Business Card</title>
<link rel="stylesheet" href="https://fonts.googleapis.com/css2?family=PT+Serif:wght@400;700&display=swap">
<style>
  :root {
    --navy-deep: #000040;
    --navy-light: #0b0b72;
    --green: #8dc63f;
    --grey: #8a8c8e;
    --grey-dark: #6d6e71;
    --silver: #c9cacc;
    --white: #ffffff;
    --backdrop: #d9d9d9;
  }
  * { box-sizing: border-box; margin: 0; padding: 0; }
  html, body {
    width: 1200px; height: 960px; overflow: hidden;
    background: var(--backdrop);
    font-family: "PT Serif", "Times New Roman", serif;
  }
  .canvas { position: relative; width: 1200px; height: 960px; }
  .card {
    position: absolute; left: 230px; width: 740px; height: 423px;
    border-radius: 22px; overflow: hidden;
    box-shadow: 0 0 0 3px var(--green), 0 14px 30px rgba(0,0,0,.25);
  }
  /* Front */
  .card--front {
    top: 38px;
    background: radial-gradient(ellipse at 70% 20%, var(--navy-light), var(--navy-deep) 75%);
    color: var(--white);
  }
  .member-badge {
    position: absolute; top: 30px; right: 46px;
    width: 58px; height: 58px; border-radius: 50%;
    border: 2px solid var(--silver);
  }
  .brand {
    position: absolute; left: 0; right: 0; display: flex; flex-direction: column; align-items: center;
  }
  .card--front .brand { top: 105px; }
  .brand__mark { width: 84px; height: 84px; border-radius: 50%; margin-bottom: 14px; }
  .card--front .brand__mark { background: var(--silver); }
  .brand__name {
    font-weight: 700; font-size: 46px; line-height: 1.02; text-align: center;
  }
  .card--front .brand__name { color: var(--silver); }
  .services {
    position: absolute; bottom: 46px; left: 0; right: 0;
    display: flex; justify-content: center; align-items: center; gap: 12px;
    font-size: 19px; color: var(--white);
  }
  .services__dot { width: 9px; height: 6px; border-radius: 50%; background: var(--green); }

  /* Back */
  .card--back { top: 499px; background: var(--white); }
  .social { position: absolute; top: 26px; right: 34px; display: flex; gap: 5px; }
  .social__icon { width: 20px; height: 20px; border-radius: 50%; background: var(--green); }
  .card--back .brand { left: 40px; right: auto; width: 330px; top: 120px; }
  .card--back .brand__mark { background: var(--grey); width: 80px; height: 80px; }
  .card--back .brand__name { color: var(--grey-dark); font-size: 40px; }
  .divider {
    position: absolute; left: 400px; top: 110px; width: 1px; height: 150px; background: var(--grey);
  }
  .contact { position: absolute; left: 428px; top: 112px; color: var(--grey-dark); }
  .contact__name { font-size: 28px; font-weight: 700; color: var(--green); line-height: 1.1; }
  .contact__role { font-size: 17px; color: var(--grey); margin-bottom: 10px; }
  .contact__list { list-style: none; font-size: 15.5px; line-height: 1.5; }
  .contact__list li { display: flex; align-items: center; gap: 8px; }
  .contact__list svg { width: 13px; height: 13px; fill: var(--green); flex: none; }
  .contact__licence { font-size: 18px; margin-top: 12px; }
</style>
</head>
<body>
<main class="canvas">

  <section class="card card--front" aria-label="Card front">
    <div class="member-badge" role="img" aria-label="The Turfcraft Guild member badge"></div>
    <div class="brand">
      <div class="brand__mark"></div>
      <div class="brand__name">Brambleton<br>Gardenworks</div>
    </div>
    <div class="services">
      <span>Residential</span><span class="services__dot"></span>
      <span>Strata</span><span class="services__dot"></span>
      <span>Commercial</span><span class="services__dot"></span>
      <span>Real Estate</span>
    </div>
  </section>

  <section class="card card--back" aria-label="Card back">
    <div class="social" aria-label="Social media">
      <span class="social__icon"></span><span class="social__icon"></span>
    </div>
    <div class="brand">
      <div class="brand__mark"></div>
      <div class="brand__name">Brambleton<br>Gardenworks</div>
    </div>
    <div class="divider"></div>
    <div class="contact">
      <div class="contact__name">Oliver Hartley</div>
      <div class="contact__role">President</div>
      <ul class="contact__list">
        <li><svg viewBox="0 0 24 24"><path d="M6.6 10.8a15.1 15.1 0 0 0 6.6 6.6l2.2-2.2a1 1 0 0 1 1-.25 11.4 11.4 0 0 0 3.6.57 1 1 0 0 1 1 1V20a1 1 0 0 1-1 1A17 17 0 0 1 3 4a1 1 0 0 1 1-1h3.5a1 1 0 0 1 1 1c0 1.25.2 2.45.57 3.57a1 1 0 0 1-.25 1z"/></svg>412-308-5571</li>
        <li><svg viewBox="0 0 24 24"><path d="M2 5h20v14H2z M2 5l10 8 10-8" fill="none" stroke="#8dc63f" stroke-width="2.4"/></svg>info@brambletongardenworks.com.au</li>
        <li><svg viewBox="0 0 24 24"><circle cx="12" cy="12" r="10"/></svg>www.brambletongardenworks.com.au</li>
      </ul>
      <div class="contact__licence">Lic. 618392K</div>
    </div>
  </section>

</main>
</body>
</html>
```